KORVAL RENOVATIONS AND CUSTOM BUILDS

5pages:
Home/ who we are , services offered, why us,
recent projects/ gallery , contact us

Industry/Entity Type

Design, renovations, project management

Coding

Coded - Design and coding required

Number of Pages Required

5+ page

Requirements
Should not have
• Too many colours

```html
<!DOCTYPE html>
<html lang="en">
<head>
<meta charset="utf-8">
<title>Korval Renovations and Custom Builds</title>
<link rel="stylesheet" href="https://fonts.googleapis.com/css2?family=Poppins:wght@300;400;500;600;700&family=Playball&display=swap">
<style>
:root{
  --navy:#1c2432;
  --navy-deep:#161d29;
  --green:#72b52d;
  --white:#ffffff;
  --text:#555a61;
  --heading:#1b1f26;
  --line:#d9dde2;
  --map:#eef0ef;
}
*{box-sizing:border-box;margin:0;padding:0}
html,body{width:1200px;height:3807px;overflow:hidden}
body{position:relative;font-family:'Poppins',sans-serif;background:var(--white);color:var(--text)}
.abs{position:absolute}

/* hero + about band */
.hero-band{left:0;top:0;width:1200px;height:1300px;background:var(--navy)}
.hero-photo{left:0;top:0;width:1200px;height:640px;background:linear-gradient(180deg,#2b313a 0%,#252c37 55%,var(--navy) 100%)}
.brand{left:59px;top:26px;color:var(--white);font-weight:500;line-height:1.1}
.brand .name{font-size:17px;letter-spacing:.3px}
.brand .tag{font-size:8px;letter-spacing:2.4px;margin-top:4px}
.brand .mark{display:inline-block;width:12px;height:12px;background:var(--green);border-radius:50%;margin-left:8px;vertical-align:middle}
.nav{top:37px;left:390px;display:flex;gap:42px;font-size:12px;color:var(--white)}
.nav .active{color:var(--green)}
.quote-btn{left:944px;top:25px;width:196px;height:36px;border:1px solid #c9ccd1;color:var(--white);font-size:12px;display:flex;align-items:center;justify-content:center;gap:10px}
.hero-title{left:0;width:1200px;top:176px;text-align:center;color:var(--white);font-weight:600;font-size:66px;line-height:78px}
.hero-script{left:0;width:1200px;top:312px;text-align:center;color:var(--green);font-family:'Playball',cursive;font-size:56px}
.discover{left:552px;top:509px}

.about-label{left:61px;top:784px;color:var(--green);font-size:12px}
.about-title{left:61px;top:816px;color:var(--white);font-size:32px;font-weight:400}
.about-title b{font-weight:600}
.exp-box{left:59px;top:872px;width:322px;height:36px;border:1px solid #3b4452;color:var(--white);font-size:15px;display:flex;align-items:center;padding-left:18px}
.exp-box span{color:var(--green);font-weight:600;margin-right:6px}
.about-text{left:61px;top:926px;width:480px;color:#d8dbe0;font-size:12.5px;line-height:21px}
.outline-btn{border:1px solid #d0d3d8;color:var(--white);font-size:12.5px;display:flex;align-items:center;justify-content:center;gap:10px}
.learn{left:59px;top:1088px;width:133px;height:38px}
.pattern-panel{left:728px;top:760px;width:215px;height:420px;background:#2c3547;transform:rotate(-5deg)}
.about-photo{left:770px;top:712px;width:362px;height:440px;background:linear-gradient(150deg,#5a6068 0%,#23272d 55%,#0d0f12 100%);transform:rotate(4deg);border:4px solid #fff}
.wave{left:0;top:1220px}

/* services */
.section-title{left:0;width:1200px;text-align:center;color:var(--heading);font-size:34px;font-weight:400;letter-spacing:.5px}
.section-title b{font-weight:600}
.svc{position:absolute;width:252px}
.svc .img{width:252px;height:240px}
.svc h3{font-size:16px;font-weight:500;color:var(--heading);margin:20px 0 8px 2px}
.svc h3.hl{color:var(--green)}
.svc p{font-size:12.5px;line-height:21px;padding-left:2px;width:230px}
.viewall{left:542px;top:1841px;width:114px;height:39px;border:1px solid var(--green);color:var(--green);font-size:12.5px;display:flex;align-items:center;justify-content:center;gap:8px}

/* project slider */
.project{left:0;top:1963px;width:1200px;height:600px;background:linear-gradient(100deg,#6d6a66 0%,#b76a3c 28%,#3a3d42 52%,#a7a29c 72%,#d8d3cc 100%)}
.project-name{left:61px;top:2440px;color:var(--white);font-size:47px;font-weight:600}
.dots{left:917px;top:2482px;width:160px;height:28px;background:#1b1f26;border-radius:14px;display:flex;align-items:center;justify-content:center;gap:24px}
.dots i{width:10px;height:10px;border-radius:50%;background:#fff;display:block}
.dots i.on{background:var(--green)}

/* why us */
.why{position:absolute;width:210px;text-align:center;top:2706px}
.why .ring{width:90px;height:90px;margin:0 auto;border:1px dashed #9bc46a;border-radius:50%;display:flex;align-items:center;justify-content:center}
.why .disc{width:74px;height:74px;border-radius:50%;background:var(--navy);display:flex;align-items:center;justify-content:center}
.why h4{color:var(--green);font-size:15.5px;font-weight:500;line-height:23px;margin-top:18px}
.why p{font-size:12.5px;line-height:21px;margin-top:16px}

.map{left:0;top:2997px;width:1200px;height:496px;background:var(--map)}

/* footer */
.footer{left:0;top:3493px;width:1200px;height:314px;background:var(--navy)}
.f-brand{left:59px;top:3570px;color:var(--white);font-weight:500}
.f-brand .name{font-size:18px;line-height:22px}
.f-brand .tag{font-size:8.5px;letter-spacing:2.4px;margin-top:3px}
.f-about{left:61px;top:3648px;width:215px;color:#d8dbe0;font-size:12px;line-height:22px}
.f-head{color:var(--green);font-size:13.5px;top:3566px}
.f-links{left:333px;top:3600px;color:#e4e6ea;font-size:12px;list-style:none}
.f-links li{height:32px}
.f-contact{left:613px;color:#e4e6ea;font-size:12px;display:flex;gap:12px;align-items:flex-start;line-height:20px}
.social{top:3600px;display:flex;gap:17px;left:888px}
.social i{display:block;width:38px;height:38px;border-radius:50%;border:1.5px solid #fff}
.social i.on{background:var(--green);border-color:var(--green)}
.f-rule{left:0;top:3766px;width:1200px;height:1px;background:#4a5362}
.copy{left:0;width:1200px;top:3778px;text-align:center;color:#e4e6ea;font-size:11.5px}
</style>
</head>
<body>

<div class="abs hero-band"></div>
<div class="abs hero-photo" role="img" aria-label="Dark modern kitchen interior with plants and shelving"></div>

<header>
  <div class="abs brand"><div class="name">KORVAL RENOVATIONS<span class="mark"></span></div><div class="tag">AND CUSTOM BUILDS</div></div>
  <nav class="abs nav"><span class="active">Home</span><span>Services Offered</span><span>Recent Projects</span><span>Contact Us</span></nav>
  <div class="abs quote-btn">Schedule A free Quote
    <svg width="22" height="12" viewBox="0 0 22 12"><path d="M1 6h18M14 1l5 5-5 5" fill="none" stroke="#fff" stroke-width="1.5"/></svg></div>
</header>

<h1 class="abs hero-title">KORVAL<br>RENOVATIONS</h1>
<div class="abs hero-script">Custom Builds</div>

<svg class="abs discover" width="96" height="96" viewBox="0 0 96 96" aria-label="Discover the project">
  <defs><path id="ring" d="M48,48 m-36,0 a36,36 0 1,1 72,0 a36,36 0 1,1 -72,0"/></defs>
  <text fill="#fff" font-family="Poppins,sans-serif" font-size="9.5" letter-spacing="3.2"><textPath href="#ring" startOffset="0">DISCOVER THE PROJECT ·</textPath></text>
  <path d="M48 30v30M38 50l10 10 10-10" fill="none" stroke="#72b52d" stroke-width="2"/>
</svg>

<section>
  <div class="abs about-label">ABOUT KORVAL RENOVATION</div>
  <h2 class="abs about-title"><b>WHO</b> WE ARE</h2>
  <div class="abs exp-box"><span>25</span> years of combined experience</div>
  <p class="abs about-text">Lorem Ipsum is simply dummy text of the printing and typesetting industry. Lorem Ipsum has been the industry's standard dummy text ever since the 1500s, when an unknown printer took a galley of type and scrambled it to make a type specimen book. It has survived not only five centuries, but also the leap into electronic typesetting, remaining essentially unchanged. It was popularised in the 1960s with the release.</p>
  <div class="abs outline-btn learn">Learn More
    <svg width="22" height="12" viewBox="0 0 22 12"><path d="M1 6h18M14 1l5 5-5 5" fill="none" stroke="#fff" stroke-width="1.5"/></svg></div>
  <div class="abs pattern-panel" role="img" aria-label="Navy backing panel with subtle pattern"></div>
  <div class="abs about-photo" role="img" aria-label="Renovated bathroom with black marble tiles and glass shower"></div>
</section>

<svg class="abs wave" width="1200" height="100" viewBox="0 0 1200 100" preserveAspectRatio="none">
  <path d="M0 55C60 40 120 60 180 50C260 40 300 45 360 42C420 40 470 60 520 30C560 5 600 0 640 20C680 40 700 72 760 72C820 72 840 40 900 35C960 30 990 55 1040 40C1100 25 1150 30 1200 35L1200 100L0 100Z" fill="#fff"/>
</svg>

<section>
  <h2 class="abs section-title" style="top:1368px"><b>SERVICES</b> &nbsp;OFFERED</h2>
  <div class="svc" style="left:59px;top:1435px"><div class="img" role="img" aria-label="Finished basement bathroom vanity" style="background:linear-gradient(180deg,#4a4a4d,#c9c9c6 60%,#8d8f92)"></div><h3>Finishing basements</h3><p>Lorem Ipsum is simply dummy text of the printing and typesetting industry.</p></div>
  <div class="svc" style="left:336px;top:1466px"><div class="img" role="img" aria-label="Interior door in a secondary legal unit" style="background:linear-gradient(90deg,#5c5e61,#cfcfcb 50%,#6a6c6f)"></div><h3>Second legal units</h3><p>Lorem Ipsum is simply dummy text of the printing and typesetting industry.</p></div>
  <div class="svc" style="left:612px;top:1435px"><div class="img" role="img" aria-label="Framed room during complete remodeling" style="background:linear-gradient(180deg,#b98a5a,#7d5a3e 55%,#9a948c)"></div><h3 class="hl">Complete Remodeling</h3><p>Lorem Ipsum is simply dummy text of the printing and typesetting industry.</p></div>
  <div class="svc" style="left:888px;top:1466px"><div class="img" role="img" aria-label="Home extension under construction" style="background:linear-gradient(180deg,#e2e3e4,#b9babb 60%,#7f8081)"></div><h3>Extensions / Additions</h3><p>Lorem Ipsum is simply dummy text of the printing and typesetting industry.</p></div>
  <div class="abs viewall">View All
    <svg width="22" height="12" viewBox="0 0 22 12"><path d="M1 6h18M14 1l5 5-5 5" fill="none" stroke="#72b52d" stroke-width="1.5"/></svg></div>
</section>

<section>
  <div class="abs project" role="img" aria-label="Modern kitchen with orange backsplash, marble island and dining area"></div>
  <h2 class="abs project-name">Project Name</h2>
  <div class="abs dots"><i></i><i class="on"></i><i></i><i></i></div>
</section>

<section>
  <h2 class="abs section-title" style="top:2636px"><b>WHY</b> US</h2>
  <div class="why" style="left:52px"><div class="ring"><div class="disc"><svg width="36" height="36" viewBox="0 0 36 36"><circle cx="18" cy="15" r="10" fill="none" stroke="#fff" stroke-width="1.6"/><path d="M18 9l2 4 4 .5-3 3 .8 4-3.8-2-3.8 2 .8-4-3-3 4-.5z" fill="none" stroke="#fff" stroke-width="1.3"/><path d="M12 23l-3 9 5-2 3 3M24 23l3 9-5-2-3 3" fill="none" stroke="#fff" stroke-width="1.3"/></svg></div></div><h4>Competitive Rates</h4><p>Lorem Ipsum is simply dummy text of the printing and typesetting industry.</p></div>
  <div class="why" style="left:276px"><div class="ring"><div class="disc"><svg width="36" height="36" viewBox="0 0 36 36"><rect x="6" y="8" width="24" height="20" rx="2" fill="none" stroke="#fff" stroke-width="1.6"/><path d="M6 13h24M12 18h6v6h-6zM21 18h5M21 22h5" fill="none" stroke="#fff" stroke-width="1.4"/></svg></div></div><h4>Licensed subcontractors</h4><p>Lorem Ipsum is simply dummy text of the printing and typesetting industry.</p></div>
  <div class="why" style="left:501px"><div class="ring"><div class="disc"><svg width="36" height="36" viewBox="0 0 36 36"><circle cx="18" cy="18" r="12" fill="none" stroke="#fff" stroke-width="1.6"/><circle cx="13" cy="14" r="2.5" fill="none" stroke="#fff" stroke-width="1.3"/><circle cx="23" cy="14" r="2.5" fill="none" stroke="#fff" stroke-width="1.3"/><circle cx="18" cy="23" r="2.5" fill="none" stroke="#fff" stroke-width="1.3"/><path d="M15 15l2 6M21 15l-2 6M15.5 14h5" stroke="#fff" stroke-width="1.2"/></svg></div></div><h4>Wide network of<br>consultants</h4><p>Lorem Ipsum is simply dummy text of the printing.</p></div>
  <div class="why" style="left:718px"><div class="ring"><div class="disc"><svg width="36" height="36" viewBox="0 0 36 36"><path d="M17 7a11 11 0 1 0 11 11H17z" fill="none" stroke="#fff" stroke-width="1.6"/><path d="M21 5v9h9A9 9 0 0 0 21 5z" fill="none" stroke="#fff" stroke-width="1.4"/><path d="M20 22h10v8H20zM20 26h10M25 22v8" fill="none" stroke="#fff" stroke-width="1.2"/></svg></div></div><h4>Suppliers list suits<br>every budget</h4><p>Lorem Ipsum is simply dummy text of the printing.</p></div>
  <div class="why" style="left:937px"><div class="ring"><div class="disc"><svg width="36" height="36" viewBox="0 0 36 36"><circle cx="18" cy="17" r="11" fill="none" stroke="#fff" stroke-width="1.6"/><path d="M18 10v7l5 3" fill="none" stroke="#fff" stroke-width="1.6"/><path d="M8 28c3 2 7 3 10 3h10" fill="none" stroke="#fff" stroke-width="1.3"/></svg></div></div><h4>Flexible working<br>hours</h4><p>Lorem Ipsum is simply dummy text of the printing.</p></div>
</section>

<div class="abs map" role="img" aria-label="Street map showing the office location"></div>

<footer>
  <div class="abs footer"></div>
  <div class="abs f-brand"><div class="name">KORVAL<br>RENOVATIONS</div><div class="tag">AND CUSTOM BUILDS</div></div>
  <p class="abs f-about">Lorem ipsum dolor sit amet, consectetur adipiscing elit, sed do eiusmod tempor...</p>

  <div class="abs f-head" style="left:331px">Site Map</div>
  <ul class="abs f-links"><li>Home</li><li>Services Offered</li><li>Recent Projects</li><li>Contact Us</li></ul>

  <div class="abs f-head" style="left:613px">Contact Us</div>
  <div class="abs f-contact" style="top:3600px">
    <svg width="20" height="22" viewBox="0 0 20 22"><path d="M10 20s7-7 7-12A7 7 0 0 0 3 8c0 5 7 12 7 12z" fill="none" stroke="#72b52d" stroke-width="1.5"/><circle cx="10" cy="8" r="2.5" fill="none" stroke="#72b52d" stroke-width="1.5"/></svg>
    <span>123 Lorem Ipsum Is A<br>dummy text.</span></div>
  <div class="abs f-contact" style="top:3653px">
    <svg width="20" height="20" viewBox="0 0 20 20"><path d="M4 2l4 1 1 4-2 1.5a10 10 0 0 0 4.5 4.5L13 11l4 1 1 4-2 2C9 18 2 11 2 4z" fill="none" stroke="#72b52d" stroke-width="1.5"/></svg>
    <span style="font-weight:600">(555)318-4470</span></div>
  <div class="abs f-contact" style="top:3698px">
    <svg width="22" height="18" viewBox="0 0 22 18"><rect x="1" y="2" width="20" height="14" fill="none" stroke="#72b52d" stroke-width="1.5"/><path d="M1 2l10 8 10-8" fill="none" stroke="#72b52d" stroke-width="1.5"/></svg>
    <span>hello@korvalbuilds.com</span></div>

  <div class="abs f-head" style="left:888px">Follow On Us</div>
  <div class="abs social"><i class="on" aria-label="Social link 1"></i><i aria-label="Social link 2"></i><i aria-label="Social link 3"></i><i aria-label="Social link 4"></i></div>

  <div class="abs f-rule"></div>
  <div class="abs copy">2022© KORVAL RENOVATIONS AND CUSTOM BUILDS. All right reserved.</div>
</footer>

</body>
</html>
```